New Plumbing Company

We are looking for a smart and creative business card design for our new plumbing company. We are looking for creativity and originality in our business cards.

Industry/Entity Type

Plumbing

Contact Information for Business Card

Kelvora Plumbing
Peter Oswalt
Managing Director
Telephone Number : 0481529046
Email : service@kelvoraplumbing.com.au
Website : www.kelvoraplumbing.com.au
Lic. 318462D

Colors
0692cd
33a6d7
000000

Requirements
Must have
• I want the business card to be designed on a black background using the blue tones i have selected as seen in the company logo.

```html
<!DOCTYPE html>
<html lang="en">
<head>
<meta charset="utf-8">
<title>Kelvora Plumbing – Business Card</title>
<link href="https://fonts.googleapis.com/css2?family=Jost:wght@400;500&display=swap" rel="stylesheet">
<style>
  :root {
    --backdrop: #a6a4a5;
    --card: #272322;
    --blue: #0692cd;
    --blue-light: #33a6d7;
    --white: #f2f2f2;
  }
  * { box-sizing: border-box; margin: 0; padding: 0; }
  html, body { width: 1200px; height: 1200px; overflow: hidden; }
  body {
    background: var(--backdrop);
    font-family: "Jost", sans-serif;
    position: relative;
  }
  .card {
    position: absolute;
    width: 642px;
    height: 378px;
    background: var(--card);
  }
  .card--front { left: 274px; top: 166px; }
  .card--back { left: 268px; top: 640px; }

  .brand {
    display: flex;
    align-items: center;
    gap: 12px;
  }
  .brand__dot {
    border: 3px solid var(--blue);
    border-radius: 50%;
    flex: none;
  }
  .brand__name {
    color: var(--blue);
    font-weight: 400;
    white-space: nowrap;
  }

  .card--front .brand {
    position: absolute;
    left: 0; right: 0; top: 0; bottom: 0;
    justify-content: center;
  }
  .card--front .brand__dot { width: 76px; height: 76px; }
  .card--front .brand__name { font-size: 42px; }

  .card--back .brand {
    position: absolute;
    left: 50px;
    top: 160px;
  }
  .card--back .brand__dot { width: 56px; height: 56px; }
  .card--back .brand__name { font-size: 23px; }

  .contact {
    position: absolute;
    left: 319px;
    top: 94px;
    color: var(--white);
  }
  .contact__name {
    color: var(--blue);
    font-size: 27px;
    font-weight: 400;
    line-height: 1;
  }
  .contact__role {
    font-size: 15px;
    margin-top: 10px;
  }
  .contact__list {
    list-style: none;
    margin-top: 30px;
  }
  .contact__item {
    display: flex;
    align-items: center;
    gap: 14px;
    font-size: 17px;
    line-height: 24px;
  }
  .contact__icon { width: 16px; height: 14px; flex: none; }
  .contact__licence {
    margin-top: 16px;
    font-size: 17px;
  }
  .contact__licence-label { color: var(--blue); }
</style>
</head>
<body>
  <section class="card card--front">
    <div class="brand">
      <span class="brand__dot"></span>
      <span class="brand__name">Kelvora Plumbing</span>
    </div>
  </section>

  <section class="card card--back">
    <div class="brand">
      <span class="brand__dot"></span>
      <span class="brand__name">Kelvora Plumbing</span>
    </div>

    <div class="contact">
      <h1 class="contact__name">Peter Oswalt</h1>
      <p class="contact__role">Managing Director</p>
      <ul class="contact__list">
        <li class="contact__item">
          <svg class="contact__icon" viewBox="0 0 16 14" aria-hidden="true">
            <path d="M1 4 Q8 -1 15 4 L13 6 L11 4.5 L5 4.5 L3 6 Z" fill="#0692cd"/>
            <rect x="3" y="7" width="10" height="6" rx="1" fill="#0692cd"/>
          </svg>
          0481529046
        </li>
        <li class="contact__item">
          <svg class="contact__icon" viewBox="0 0 16 14" aria-hidden="true">
            <circle cx="8" cy="7" r="6" fill="none" stroke="#0692cd" stroke-width="1.4"/>
            <ellipse cx="8" cy="7" rx="2.6" ry="6" fill="none" stroke="#0692cd" stroke-width="1.2"/>
            <line x1="2" y1="7" x2="14" y2="7" stroke="#0692cd" stroke-width="1.2"/>
          </svg>
          www.kelvoraplumbing.com.au
        </li>
        <li class="contact__item">
          <svg class="contact__icon" viewBox="0 0 16 14" aria-hidden="true">
            <rect x="1" y="2" width="14" height="10" fill="#0692cd"/>
            <path d="M1 2 L8 8 L15 2" fill="none" stroke="#272322" stroke-width="1.3"/>
          </svg>
          service@kelvoraplumbing.com.au
        </li>
      </ul>
      <p class="contact__licence"><span class="contact__licence-label">LIC.</span> 318462D</p>
    </div>
  </section>
</body>
</html>
```